Broschüre für Spezialist für den Transfer von mobil eingeschränkten Personen
Zielgruppe
Wir sind Spezialist für den Transfer von mobil eingeschränkten Personen. Unsere Zielgruppe für dieses Projekt sind (öffentliche) Schwimmbäder, Planer und Architekten.
Aufgabenstellung
Es soll unsere aktuelle Broschüre neu aufgesetzt werden. Diese hat aktuell 12 Seiten. Es sollen aber noch zwei weitere Produkte hinzu kommen, so dass wir auf 14 Seiten kommen werden. Eventuell werden wir auch noch Zubehör mit rein nehmen, so dass wir dann auf 16 Seiten kommen. Die aktuelle Broschüre habe ich Ihnen angehängt. Texte und Bilder können für einen ersten Entwurf gerne übernommen werden.
Seite 1 - 12 sollen übernommen werden
Seite 13 o-dive4 (https://www.bervamosrl.example/de/o-dive4-lift-fuer-schwimmbecken/)
Seite 14 o-dive5 (https://www.bervamosrl.example/de/o-dive5-lifte-fuer-schwimmbecken/)

```html
<!DOCTYPE html>
<html lang="de">
<head>
<meta charset="utf-8">
<title>Neuheit Hebelotse – Broschürenseite 01</title>
<link rel="stylesheet" href="https://fonts.googleapis.com/css2?family=Fjalla+One&family=Jost:wght@400;500;700&display=swap">
<style>
  :root {
    --backdrop: #e3e4e6;
    --paper: #f2f3f5;
    --band: #14a8e6;
    --ink: #1f2533;
    --ink-soft: #2b3650;
    --white: #ffffff;
  }
  * { box-sizing: border-box; margin: 0; padding: 0; }
  html, body { width: 1200px; height: 1200px; overflow: hidden; }
  body {
    background: var(--backdrop);
    font-family: "Jost", "Futura", sans-serif;
    color: var(--ink);
    position: relative;
  }
  .page {
    position: absolute;
    left: 195px; top: 20px;
    width: 810px; height: 1160px;
    background: var(--paper);
    overflow: hidden;
    box-shadow: 0 6px 24px rgba(0,0,0,.12);
  }
  .page__shapes { position: absolute; inset: 0; }
  .hero-photo, .product-photo { position: absolute; left: 0; top: 0; }
  .headline {
    position: absolute; left: 70px; top: 392px;
    font-family: "Fjalla One", "Oswald", sans-serif;
  }
  .headline__title { font-size: 46px; line-height: 1.1; color: var(--ink); font-weight: 400; }
  .headline__sub { font-size: 18px; color: var(--ink); margin-top: 2px; }
  .product-photo {
    left: 105px; top: 505px;
  }
  .caption {
    position: absolute; left: 440px; top: 620px; width: 240px;
    border-left: 5px solid var(--band);
    padding-left: 12px;
    font-size: 16px; line-height: 1.25; color: var(--ink);
  }
  .features {
    position: absolute; left: 70px; top: 800px; width: 700px;
    display: grid; grid-template-columns: 320px 320px; column-gap: 50px;
  }
  .features__heading {
    grid-column: 1 / 2;
    color: var(--white); font-weight: 500; font-size: 17px; margin-bottom: 16px;
  }
  .features__col--right { grid-row: 1 / 3; grid-column: 2; margin-top: -20px; }
  .features__intro { font-weight: 700; font-size: 16px; line-height: 1.25; margin-bottom: 14px; }
  .features__list { list-style: none; font-size: 15.5px; line-height: 1.22; color: var(--ink-soft); }
  .features__list li { margin-bottom: 14px; }
  .page-number {
    position: absolute; left: 520px; top: 1110px;
    font-weight: 700; font-size: 16px; color: var(--ink);
  }
</style>
</head>
<body>
  <article class="page">
    <svg class="page__shapes" width="810" height="1160" viewBox="0 0 810 1160" aria-hidden="true">
      <defs>
        <linearGradient id="bandGrad" x1="0" y1="0" x2="1" y2="0">
          <stop offset="0" stop-color="#15a9e8"/>
          <stop offset="1" stop-color="#1690d6"/>
        </linearGradient>
        <linearGradient id="iceGrad" x1="0" y1="0" x2="1" y2="0">
          <stop offset="0" stop-color="#7cc4e6"/>
          <stop offset="1" stop-color="#c6e4f2"/>
        </linearGradient>
      </defs>
      <rect x="0" y="740" width="810" height="420" fill="url(#bandGrad)"/>
      <polygon points="420,580 810,330 810,730" fill="url(#iceGrad)" opacity=".85"/>
    </svg>

    <svg class="hero-photo" width="810" height="380" viewBox="0 0 810 380" role="img"
         aria-label="Foto: mobiler Schwimmbadlifter mit Sitz am Beckenrand eines Freibads, Steuerung markiert">
      <defs>
        <linearGradient id="heroGrad" x1="0" y1="0" x2="1" y2="0">
          <stop offset="0" stop-color="#44c6e0"/>
          <stop offset=".55" stop-color="#38b4d6"/>
          <stop offset=".7" stop-color="#a49290"/>
          <stop offset="1" stop-color="#8f8281"/>
        </linearGradient>
      </defs>
      <polygon points="0,0 810,0 810,250 0,370" fill="url(#heroGrad)"/>
      <circle cx="485" cy="115" r="65" fill="none" stroke="#ffffff" stroke-width="3"/>
    </svg>

    <header class="headline">
      <h1 class="headline__title">Neuheit Hebelotse</h1>
      <p class="headline__sub">Unser neuer Standard für alle mobilen und semi-portablen KLV-Schwimmbadlifter.</p>
    </header>

    <svg class="product-photo" width="320" height="255" viewBox="0 0 320 255" role="img"
         aria-label="Produktfoto: Steuerbox mit Not-Stopp-Taste, Handschalter mit Spiralkabel und Aktivierungsschlüssel">
      <rect x="20" y="0" width="105" height="255" rx="8" fill="#dcdde0"/>
      <rect x="140" y="55" width="55" height="190" rx="20" fill="#e6e7ea"/>
      <rect x="220" y="35" width="75" height="28" rx="6" fill="#2a2c31"/>
    </svg>

    <p class="caption">Der Aktivierungsschlüssel verhindert eine unberechtigte Nutzung des Liftsystems (optional)</p>

    <section class="features">
      <h2 class="features__heading">Hebelotse – die intelligente Steuerung</h2>
      <div class="features__col features__col--left">
        <p class="features__intro">Der Hebelotse ist die modernste Schwimmbadlift Steuerung auf dem Markt. Er vereint Selbst-Diagnose, Energie-Management, Sicherheits- und Überwachungs-Funktionen in einem zeitlosen Design.</p>
        <ul class="features__list">
          <li>abwärtskompatibel mit allen mobilen KLV-Schwimmbadliftern und vielen Wettbewerbsprodukten</li>
          <li>mehr Hebezyklen mit einer Akkuladung</li>
          <li>akustisches Nutzer-Warnsignal über Handschalter aktivierbar</li>
        </ul>
      </div>
      <div class="features__col features__col--right">
        <ul class="features__list">
          <li>Not-Stop Funktion mit akustischem Warnsignal</li>
          <li>farbige LEDs zeigen eindeutig den Ladezustand des Liftsystems</li>
          <li>Service-Status LED zur Einhaltung der Wartungsvorschriften</li>
          <li>Nutzungdatenspeicher für Wartungs-, Garantie- und Servicearbeiten</li>
          <li>Sicherungsplatte zum Abschließen des Wechselakkus</li>
          <li>optionaler Aktivierungsschlüssel schützt Ihr Liftsystem</li>
        </ul>
      </div>
    </section>

    <span class="page-number">01</span>
  </article>
</body>
</html>
```